Breezeway Climate Business Card Design

Design new, 2 sides, business cards for a residential and light commercial heating, air conditioning contractor.

Target Market(s)

Homeowners, small businesses

Industry/Entity Type

Business

Contact Information for Business Card

Dominic Vasquerelli
Phone - 555-214-6837
Email
Address - PO box 618
Millbrook NJ 07999
Website - www.BreezewayClimateLLC.example

Requirements
Must have
• logo, company colors, standard size with no die cut, so I can use printhaven

```html
<!DOCTYPE html>
<html lang="en">
<head>
<meta charset="utf-8">
<title>Breezeway Climate – Business Card</title>
<link rel="stylesheet" href="https://fonts.googleapis.com/css2?family=EB+Garamond:wght@400;600&display=swap">
<style>
  :root {
    --page: #ece8e2;
    --card-white: #ffffff;
    --card-peach-light: #fffaf5;
    --card-peach: #f7dcc4;
    --maroon: #8e1524;
    --maroon-deep: #6e0d1a;
    --maroon-bright: #a81c2e;
    --gold: #f0a030;
    --gold-line: #d9822b;
    --ink-light: #fbeee6;
  }
  * { box-sizing: border-box; margin: 0; padding: 0; }
  html, body { width: 1200px; height: 802px; overflow: hidden; }
  body {
    background: var(--page);
    display: flex;
    align-items: center;
    justify-content: center;
    gap: 40px;
    font-family: "EB Garamond", Garamond, serif;
  }
  .card {
    position: relative;
    width: 540px;
    height: 309px;
    border-radius: 18px;
    overflow: hidden;
    box-shadow: 0 6px 18px rgba(0,0,0,0.18);
  }
  .card--front {
    background: var(--card-white);
    display: flex;
    align-items: center;
    justify-content: center;
    gap: 16px;
  }
  .brand-dot {
    width: 26px; height: 26px;
    border-radius: 50%;
    background: var(--gold);
  }
  .brand-name {
    font-size: 46px;
    font-weight: 600;
    color: var(--maroon);
    letter-spacing: 1px;
  }
  .card--back {
    background: linear-gradient(135deg, var(--card-peach-light) 0%, var(--card-white) 35%, var(--card-peach) 100%);
  }
  .panel-frame {
    position: absolute;
    left: 0; top: 0;
    width: 540px; height: 309px;
  }
  .contact {
    position: absolute;
    left: 130px; top: 52px;
    width: 280px;
    text-align: center;
    color: var(--ink-light);
  }
  .contact__name {
    font-size: 24px;
    font-weight: 600;
    color: #ffffff;
    letter-spacing: 0.5px;
  }
  .contact__rule {
    height: 1px;
    margin: 10px 10px;
    background: var(--gold-line);
  }
  .contact__line {
    font-size: 16px;
    line-height: 1.35;
  }
  .contact__web { font-size: 17px; }
</style>
</head>
<body>
  <section class="card card--front" aria-label="Business card front">
    <span class="brand-dot"></span>
    <span class="brand-name">Breezeway Climate</span>
  </section>

  <section class="card card--back" aria-label="Business card back">
    <svg class="panel-frame" viewBox="0 0 540 309" aria-hidden="true">
      <defs>
        <radialGradient id="panel-fill" cx="50%" cy="45%" r="60%">
          <stop offset="0" stop-color="#a81c2e"/>
          <stop offset="1" stop-color="#6e0d1a"/>
        </radialGradient>
      </defs>
      <rect x="104" y="30" width="332" height="249" rx="22" fill="#ffffff"/>
      <rect x="110" y="36" width="320" height="237" rx="18" fill="#f0a030"/>
      <rect x="117" y="43" width="306" height="223" rx="14" fill="url(#panel-fill)"/>
    </svg>
    <div class="contact">
      <p class="contact__name">Dominic Vasquerelli</p>
      <div class="contact__rule"></div>
      <p class="contact__line">PO box 618</p>
      <p class="contact__line">Millbrook NJ 07999</p>
      <p class="contact__line">555-214-6837</p>
      <div class="contact__rule"></div>
      <p class="contact__line contact__web">www.BreezewayClimateLLC.example</p>
    </div>
  </section>
</body>
</html>
```